Harvest Velmora website and logo design

Looking to create a personal finance service website. My goal is for this website to be a resource repository where potential clients could come to get resources that they may find helpful for their personal use. I would like the website to have ways to collect emails from people who visit my website so I can send them periodic newsletters. I would like the website to have the following sections: A blog page, a resource page, a book review page (with potential affiliate links), An icon for a link to my podcast link ( titled Coin Climbers Working of getting this off the ground) ( I need a design for this podcast page as well) (coin climbers podcast is intended to interview everyday people who are on their journey to creating wealth, interview them and find out what is working for them) (design inspiration is an individual stacking a pile of gold) a section asking people to schedule a strategy coaching call, an about page.

I currently have a website with Word press titled Keliruston.com. The fron page should be about mira and a link to the harvest velmor platform. I would like to house harvest velmora on this site. I currently do not have a logo for harvest Velmora as well so I would like that or I can create a logo design request? The tag line should be Harvest Velmora… beside you. Helping your money grow branches.

The atmosphere I would like to have set for the site is that of calming colors that will put people at ease. The color green (vibrant green like that of a leaf) and gold is what I have in mind as my main color.
The vision of logo I have in mind to be incorporated through the website is that off a tree filled with money. The tree should have many roots and Money should be flowing through different channels of the roots. The goal is to teach people to give their money roots to go where they intend it to go rather than them wondering where their money went to every month.

The name of my business is harvest Velmora (pronounced: Velmoira). The idea is that harvest velmora with you. It does not escape you. So you are like a try planted and your money goes to where you intend them to go. You are intentional about your finance.

Target audience is men and women between the ages of 25-45. Core age is about 30 though. My targeted audience is the person who desires to have control over their finances by taking the appropriate action necessary. they are action oriented and go getters. They like to have resources at hand that will help them make informed decisions.
I would like images of real people looking at peace with the state of their well being.
Examples of websites I like are:
www.brightpursefolio.com/
https://www.tradelantern.com/
https://www.nadiquerovan.com/
https://velquist.tv/
https://maribelthorncrest.com/

Target Market(s)

Men and Women of all Race age 25-35

Logo Text

Harvest Velmora

Coding

Coded - Design and coding required

Number of Pages Required

4 page

Font styles to use
Serif
Decorative

Colors

Designer to choose colors to be used in the design.

```html
<!DOCTYPE html>
<html lang="en">
<head>
<meta charset="utf-8">
<title>Harvest Velmora</title>
<link rel="stylesheet" href="https://fonts.googleapis.com/css2?family=Saira:wght@400;500;600;700&family=Roboto:ital,wght@0,400;0,500;1,400&display=swap">
<style>
:root{
  --green:#1f7d3b;
  --green-dark:#17612d;
  --gold:#e09d0a;
  --ink:#222;
  --muted:#555;
  --grey-band:#e9e9e9;
  --footer-bg:#f5f5f9;
  --white:#fff;
}
*{box-sizing:border-box;margin:0;padding:0}
html,body{width:1200px;height:3628px;overflow:hidden}
body{position:relative;background:var(--white);font-family:"Roboto",Arial,sans-serif;color:var(--ink)}
.abs{position:absolute}
.heading{font-family:"Saira",Arial,sans-serif}

/* header */
.site-header{left:0;top:0;width:1200px;height:118px;background:var(--white);z-index:3}
.nav-link{font-family:"Saira",Arial,sans-serif;font-weight:600;font-size:14px;top:76px;color:var(--ink);text-transform:uppercase}
.nav-link.active{color:var(--green)}
.logo-tab{left:437px;top:0;width:326px;height:146px;z-index:4}
.brand-name{font-family:"Saira",Arial,sans-serif;font-weight:700;color:var(--ink);white-space:nowrap}
.logo-tab .brand-name{position:absolute;left:0;width:326px;top:86px;text-align:center;font-size:33px;line-height:1}
.logo-tab .brand-dot{position:absolute;left:143px;top:18px;width:40px;height:40px;border-radius:50%;background:var(--green)}
.call{left:772px;top:22px;font-family:"Saira",Arial,sans-serif;font-weight:600;font-size:23px;color:var(--gold);display:flex;align-items:center;gap:8px}
.call-icon{width:30px;height:30px;border-radius:50%;background:var(--gold);display:flex;align-items:center;justify-content:center}

/* hero */
.hero{left:0;top:118px;width:1200px;height:623px;background:linear-gradient(90deg,#4f5a4c 0%,#6b6e66 35%,#8a7d70 60%,#6e6258 100%)}
.hero-title{left:172px;top:337px;font-family:"Saira",Arial,sans-serif;font-weight:600;font-size:44px;line-height:50px;color:var(--white);width:520px}
.hero-arrow{top:402px}

/* resources */
.resources{left:0;top:741px;width:1200px;height:605px;background:var(--grey-band)}
.section-title{font-family:"Saira",Arial,sans-serif;font-weight:600;font-size:41px;color:var(--ink);text-align:center;width:1200px;left:0}
.card{top:887px;width:199px;height:359px;background:var(--white)}
.card-img{width:199px;height:155px}
.card h3{font-family:"Saira",Arial,sans-serif;font-weight:500;font-size:16px;line-height:21px;margin:18px 14px 10px;color:var(--ink)}
.card p{font-size:11px;line-height:17px;color:var(--muted);margin:0 14px}
.btn{display:inline-block;background:var(--gold);color:var(--white);font-family:"Saira",Arial,sans-serif;font-weight:500}
.card .btn{position:absolute;left:18px;top:311px;font-size:12px;padding:6px 14px}

/* blog */
.blog-meta{font-family:"Saira",Arial,sans-serif;font-weight:600;font-size:13px;color:var(--green)}
.blog-head{font-family:"Saira",Arial,sans-serif;font-weight:500;font-size:18px;line-height:23px;color:#333;text-transform:uppercase}
.blog-text{font-size:11px;line-height:19px;color:var(--muted)}

/* podcast */
.podcast{left:0;top:1960px;width:1200px;height:497px}
.podcast-title{left:172px;top:2040px;font-family:"Saira",Arial,sans-serif;font-weight:700;font-size:41px;line-height:47px;color:var(--white);width:380px}
.podcast-text{left:172px;top:2202px;font-size:16px;line-height:23px;color:var(--white);width:350px}
.podcast-btn{left:172px;top:2326px;width:153px;height:42px;background:var(--green);color:var(--white);font-family:"Saira",Arial,sans-serif;font-weight:600;font-size:16px;display:flex;align-items:center;justify-content:center;gap:7px}

/* reviews */
.review{top:2577px;width:270px;height:204px;background:var(--white);border:1px solid #e6e6e6;box-shadow:0 0 6px rgba(0,0,0,.06)}
.avatar{position:absolute;left:17px;top:17px;width:66px;height:66px;border-radius:50%;background:linear-gradient(135deg,#c9b39a,#7f8aa0)}
.review h4{position:absolute;left:96px;top:16px;font-family:"Saira",Arial,sans-serif;font-weight:600;font-size:16px;color:var(--green)}
.review p{position:absolute;left:96px;top:50px;width:162px;font-style:italic;font-size:12px;line-height:21px;color:#666}
.book-btn{left:539px;top:2813px;width:121px;height:45px;font-size:18px;display:flex;align-items:center;justify-content:center}

/* newsletter */
.newsletter{left:0;top:2914px;width:1200px;height:360px;background:var(--green)}
.news-title{top:3000px;color:var(--white)}
.news-text{left:0;width:1200px;top:3060px;text-align:center;font-size:14px;line-height:23px;color:var(--white)}
.field{top:3144px;width:247px;height:33px;border-bottom:2px solid var(--gold);color:var(--white);font-size:13px;padding-top:4px}
.signup{left:802px;top:3131px;width:122px;height:45px;font-size:18px;display:flex;align-items:center;justify-content:center}

/* footer */
.site-footer{left:0;top:3274px;width:1200px;height:354px;background:var(--footer-bg)}
.footer-brand{left:170px;top:3360px;font-size:35px}
.footer-dot{left:272px;top:3326px;width:34px;height:34px;border-radius:50%;background:var(--green)}
.social{top:3460px;width:20px;height:20px;border-radius:50%;background:#222}
.foot-col h5{font-family:"Saira",Arial,sans-serif;font-weight:500;font-size:16px;color:#333;margin-bottom:13px}
.foot-col li{list-style:none;font-size:11px;line-height:22px;color:#444}
.foot-rule{left:170px;top:3556px;width:856px;height:1px;background:#ccc}
.copyright{left:0;width:1200px;top:3588px;text-align:center;font-size:12px;color:#333}
</style>
</head>
<body>

<header class="site-header abs">
  <a class="nav-link active abs" style="left:173px">Home</a>
  <a class="nav-link abs" style="left:259px">About</a>
  <a class="nav-link abs" style="left:346px">Services</a>
  <a class="nav-link abs" style="left:766px">Reviews</a>
  <a class="nav-link abs" style="left:869px">Blog</a>
  <a class="nav-link abs" style="left:944px">Contact Us</a>
  <div class="call abs">
    <span class="call-icon"><svg width="15" height="15" viewBox="0 0 24 24"><path fill="#fff" d="M6.6 10.8c1.4 2.8 3.8 5.1 6.6 6.6l2.2-2.2c.3-.3.7-.4 1-.2 1.1.4 2.3.6 3.6.6.6 0 1 .4 1 1V20c0 .6-.4 1-1 1C10.6 21 3 13.4 3 4c0-.6.4-1 1-1h3.5c.6 0 1 .4 1 1 0 1.3.2 2.5.6 3.6.1.3 0 .7-.2 1L6.6 10.8z"/></svg></span>
    Call: (555)-302-7719
  </div>
</header>

<div class="logo-tab abs">
  <svg class="abs" width="326" height="146" viewBox="0 0 326 146"><path d="M0 118 L13 146 L313 146 L326 118 L326 0 L0 0 Z" fill="#fff"/></svg>
  <span class="brand-dot"></span>
  <span class="brand-name">Harvest Velmora</span>
</div>

<section class="hero abs" role="img" aria-label="Photo of a smiling man in glasses reading a tablet in a bright living room"></section>
<h1 class="hero-title abs">Harvest Velmora… beside you. Helping your money grow branches.</h1>
<svg class="hero-arrow abs" style="left:34px" width="36" height="62" viewBox="0 0 36 62"><path d="M32 3 L5 31 L32 59" fill="none" stroke="#fff" stroke-width="4"/></svg>
<svg class="hero-arrow abs" style="left:1124px" width="36" height="62" viewBox="0 0 36 62"><path d="M4 3 L31 31 L4 59" fill="none" stroke="#fff" stroke-width="4"/></svg>

<section class="resources abs"></section>
<h2 class="section-title abs" style="top:796px">Resources</h2>

<article class="card abs" style="left:172px">
  <div class="card-img" role="img" aria-label="Photo of a man working on a laptop by a window" style="background:linear-gradient(135deg,#dcd9d2,#8a6b4c)"></div>
  <h3>Finibuso losernorum lormetalorum</h3>
  <p>Lorem ipsum dolor sit alimet consectetur adipiscing elolits ddo eiusmod tempor incilodi unt ut labore et dololorrc.</p>
  <a class="btn">Read More</a>
</article>
<article class="card abs" style="left:391px">
  <div class="card-img" role="img" aria-label="Photo of a seedling growing on rising stacks of coins" style="background:linear-gradient(135deg,#eee7d4,#b89a4a)"></div>
  <h3>Finibuso losernorum lormetalorum</h3>
  <p>Lorem ipsum dolor sit alimet consectetur adipiscing elolits ddo eiusmod tempor incilodi unt ut labore et dololorrc.</p>
  <a class="btn">Read More</a>
</article>
<article class="card abs" style="left:610px">
  <div class="card-img" role="img" aria-label="Photo of a couple looking at a laptop together" style="background:linear-gradient(135deg,#e2e0dc,#5a6f8a)"></div>
  <h3>Finibuso losernorum lormetalorum</h3>
  <p>Lorem ipsum dolor sit alimet consectetur adipiscing elolits ddo eiusmod tempor incilodi unt ut labore et dololorrc.</p>
  <a class="btn">Read More</a>
</article>
<article class="card abs" style="left:829px">
  <div class="card-img" role="img" aria-label="Photo of hands holding a pink piggy bank" style="background:linear-gradient(135deg,#d8b9a6,#a87a6a)"></div>
  <h3>Finibuso losernorum lormetalorum</h3>
  <p>Lorem ipsum dolor sit alimet consectetur adipiscing elolits ddo eiusmod tempor incilodi unt ut labore et dololorrc.</p>
  <a class="btn">Read More</a>
</article>

<h2 class="section-title abs" style="top:1400px">Latest Blog Posts</h2>

<div class="abs" role="img" aria-label="Photo of a woman reviewing paperwork at a kitchen table with a laptop" style="left:172px;top:1483px;width:415px;height:277px;background:linear-gradient(135deg,#c9b8a8,#e3e7df 55%,#6a6b68)"></div>
<h3 class="blog-head abs" style="left:172px;top:1779px">Finibus bonorum et malorum</h3>
<p class="blog-text abs" style="left:172px;top:1811px;width:410px">Sed ut perspiciatis undloree omnis iste natus error sit voluptatem accusaloren tium doloremque laudantium, totloram rem aperiam, eaque ipsa.</p>
<p class="blog-meta abs" style="left:172px;top:1859px">APR 02 2020</p>

<div class="abs" role="img" aria-label="Photo of cupped hands in a dark suit with green dollar signs" style="left:605px;top:1483px;width:206px;height:187px;background:linear-gradient(135deg,#3b3b38,#1d1e1c)"></div>
<h3 class="blog-head abs" style="left:828px;top:1499px;width:220px">Finibus bonorum et malorum</h3>
<p class="blog-text abs" style="left:828px;top:1551px;width:200px">Sed ut perspiciatis undloree omnis iste natus error sit voluptatem accusaloren tium doloremque laudantium, totloram rem aperiam, eaque ipsa.</p>
<p class="blog-meta abs" style="left:831px;top:1637px">APR 02 2020</p>

<div class="abs" role="img" aria-label="Photo of a calculator, glasses and documents on a desk" style="left:605px;top:1687px;width:206px;height:187px;background:linear-gradient(135deg,#e4e7ea,#8e9aa6)"></div>
<h3 class="blog-head abs" style="left:828px;top:1704px;width:220px">Finibus bonorum et malorum</h3>
<p class="blog-text abs" style="left:828px;top:1756px;width:200px">Sed ut perspiciatis undloree omnis iste natus error sit voluptatem accusaloren tium doloremque laudantium, totloram rem aperiam, eaque ipsa.</p>
<p class="blog-meta abs" style="left:831px;top:1842px">APR 02 2020</p>

<section class="podcast abs">
  <div class="abs" role="img" aria-label="Photo of a woman in a yellow sweater and glasses working at a desk" style="left:500px;top:0;width:700px;height:497px;background:linear-gradient(120deg,#5d5a52,#9a8f7a 50%,#4a4944)"></div>
  <svg class="abs" style="left:0;top:0" width="662" height="497" viewBox="0 0 662 497"><polygon points="0,0 549,0 662,497 0,497" fill="#e09d0a"/></svg>
</section>
<h2 class="podcast-title abs">Coin Climbers Working of getting this off the ground</h2>
<p class="podcast-text abs">Lorem ipsum dolor sit amet, consectetur adipci ng elit, sed do eiusmod tempor incididunt ut la bore et dolore magna aliquat enim ad minim veniam, quis nostrud exercitation.</p>
<a class="podcast-btn abs">
  <svg width="18" height="18" viewBox="0 0 24 24" fill="none" stroke="#fff" stroke-width="2"><circle cx="12" cy="11" r="3"/><path d="M12 14v8M6.3 16.5a8 8 0 1 1 11.4 0"/></svg>
  My Podcast
</a>

<h2 class="section-title abs" style="top:2500px">Reviews</h2>
<article class="review abs" style="left:173px">
  <span class="avatar" role="img" aria-label="Reviewer portrait"></span>
  <h4>Dorian</h4>
  <p>"Lorem ipsum dolor sit met conse ctetur adipiscing elie do iusmod tempm ipsumdo lor sit amet, consectetulorr adipl oorem ipsumdo lsec teturlore adipisdo"</p>
</article>
<article class="review abs" style="left:465px">
  <span class="avatar" role="img" aria-label="Reviewer portrait"></span>
  <h4>Talsia</h4>
  <p>"Lorem ipsum dolor sit met conse ctetur adipiscing elie do iusmod tempm ipsumdo lor sit amet, consectetulorr adipl oorem ipsumdo lsec teturlore adipisdo"</p>
</article>
<article class="review abs" style="left:757px">
  <span class="avatar" role="img" aria-label="Reviewer portrait"></span>
  <h4>Wren Hollis</h4>
  <p>"Lorem ipsum dolor sit met conse ctetur adipiscing elie do iusmod tempm ipsumdo lor sit amet, consectetulorr adipl oorem ipsumdo lsec teturlore adipisdo"</p>
</article>
<a class="btn book-btn abs">Book Now</a>

<section class="newsletter abs"></section>
<h2 class="section-title news-title abs">Our Newsletter</h2>
<p class="news-text abs">Lorem ipsum dolor sit amet, consectetur adipiscing elit, sed do eiusmod<br>tempor incididunt ut labore et dolore magna alenim ad minim</p>
<div class="field abs" style="left:275px">Name:</div>
<div class="field abs" style="left:537px">Email:</div>
<a class="btn signup abs">Sign Up</a>

<footer class="site-footer abs"></footer>
<span class="footer-dot abs"></span>
<span class="brand-name footer-brand abs">Harvest Velmora</span>
<span class="social abs" style="left:217px" aria-label="Social link"></span>
<span class="social abs" style="left:258px" aria-label="Social link"></span>
<span class="social abs" style="left:300px" aria-label="Social link"></span>
<span class="social abs" style="left:340px" aria-label="Social link"></span>
<span class="social abs" style="left:380px" aria-label="Social link"></span>

<div class="foot-col abs" style="left:521px;top:3320px">
  <h5>Company</h5>
  <ul><li>Lorem ipsum dolo</li><li>Consectetur adipist.</li><li>Fusce eget leo tincid</li><li>Donec consequat</li><li>Praesent elementum</li><li>Jmauris posueret</li></ul>
</div>
<div class="foot-col abs" style="left:713px;top:3320px">
  <h5>Information</h5>
  <ul><li>Lorem ipsum dolo</li><li>Consectetur adipit.</li><li>Fusce eget leo tincid</li><li>Donec consequat</li><li>Praesent elementum</li><li>Jmauris posuer</li></ul>
</div>
<div class="foot-col abs" style="left:898px;top:3320px">
  <h5>Other Links</h5>
  <ul><li>Lorem ipsum dolo</li><li>Consectetuscing elit.</li><li>Fusce eget leo tincid</li><li>Donec consequat</li><li>Praesent elementum</li><li>Jmauris posueret</li></ul>
</div>
<div class="foot-rule abs"></div>
<p class="copyright abs">Copyright 2020 Harvest Velmora. All Rights Reserved. Terms of Use | Privacy Policy | Disclosures</p>

</body>
</html>
```